Business Card Design

I already have a company logo for my company. I have a logo for the manufacturer we represent. I want a professional business card design.

```html
<!DOCTYPE html>
<html lang="en">
<head>
<meta charset="utf-8">
<title>Signalpoint Safety LLC – Business Card</title>
<link rel="stylesheet" href="https://fonts.googleapis.com/css2?family=Poppins:wght@400;500;700;800&display=swap">
<style>
  :root {
    --stage: #2e2e2e;
    --card-white: #ffffff;
    --card-black: #070707;
    --brand-red: #e3202b;
    --brand-gold: #d9a520;
    --ink: #1b1b1b;
    --wash: rgba(227, 32, 43, 0.08);
  }
  * { margin: 0; padding: 0; box-sizing: border-box; }
  html, body {
    width: 1200px; height: 866px; overflow: hidden;
    background: var(--stage);
    font-family: "Poppins", sans-serif;
  }
  .stage {
    width: 1200px; height: 866px;
    display: flex; flex-direction: column; align-items: center;
    justify-content: center; gap: 22px;
  }
  .card {
    position: relative; width: 700px; height: 400px; overflow: hidden;
    box-shadow: 0 10px 24px rgba(0,0,0,0.45);
  }
  .card-front { background: var(--card-white); }
  .card-back { background: var(--card-black); }

  .front-shapes { position: absolute; inset: 0; }

  .decor-wash {
    position: absolute; left: 40px; top: 0; width: 250px; height: 230px;
    background: linear-gradient(135deg, rgba(220,220,220,0.35), rgba(217,165,32,0.10) 55%, rgba(255,255,255,0));
  }

  .contact-block { position: absolute; left: 40px; top: 96px; }
  .person-name {
    color: var(--brand-red); font-weight: 800; font-size: 25px;
    letter-spacing: 1px; text-transform: uppercase; line-height: 1.1;
  }
  .person-role { color: var(--ink); font-size: 17px; margin-top: 2px; }
  .contact-rule {
    width: 300px; height: 1px; background: var(--brand-gold); margin: 10px 0 10px;
  }
  .contact-line {
    display: flex; align-items: center; gap: 10px;
    color: var(--ink); font-size: 16px; line-height: 1.55;
  }
  .contact-line svg { width: 15px; height: 15px; flex: none; }

  .front-brand {
    position: absolute; right: 48px; top: 118px;
    display: flex; align-items: center; gap: 12px;
  }
  .brand-dot {
    width: 22px; height: 22px; border-radius: 50%; background: var(--brand-red);
  }
  .brand-name {
    color: var(--brand-red); font-weight: 800; font-size: 30px;
    letter-spacing: 1px; text-transform: uppercase; line-height: 1.05;
  }

  .address-block {
    position: absolute; right: 40px; top: 252px; text-align: right;
    color: var(--ink); font-size: 16px; line-height: 1.4;
  }
  .address-rule {
    position: absolute; right: 40px; top: 308px; width: 340px; height: 1px;
    background: var(--brand-gold);
  }
  .website {
    position: absolute; right: 40px; bottom: 14px;
    color: #ffffff; font-size: 17px; letter-spacing: 0.5px;
  }

  .back-brand {
    position: absolute; inset: 0;
    display: flex; align-items: center; justify-content: center; gap: 18px;
  }
  .back-brand .brand-dot { width: 36px; height: 36px; }
  .back-brand .brand-name { font-size: 44px; }
</style>
</head>
<body>
<main class="stage">

  <section class="card card-front" aria-label="Business card front">
    <svg class="front-shapes" viewBox="0 0 700 400" width="700" height="400" aria-hidden="true">
      <polygon points="0,250 380,120 560,120 180,290 0,320" fill="var(--wash)"/>
      <rect x="0" y="343" width="280" height="4" fill="var(--brand-red)"/>
      <path d="M700 343 H262 C236 343 232 400 200 400 H700 Z" fill="var(--card-black)"/>
    </svg>

    <div class="decor-wash" role="img" aria-label="Faint background brand decoration"></div>

    <div class="contact-block">
      <p class="person-name">Jonathan Smith</p>
      <p class="person-role">Managing Director</p>
      <div class="contact-rule"></div>
      <p class="contact-line">
        <svg viewBox="0 0 16 16" aria-hidden="true"><path d="M4 1.5 6.2 4.2 5 6a8 8 0 0 0 5 5l1.8-1.2 2.7 2.2-1.4 2.2C7 14 2 9 1.8 2.9Z" fill="var(--brand-red)"/></svg>
        044-123 456 789
      </p>
      <p class="contact-line">
        <svg viewBox="0 0 16 16" aria-hidden="true"><rect x="1" y="3" width="14" height="10" fill="var(--brand-red)"/><path d="M1 3 8 9 15 3" fill="none" stroke="#fff" stroke-width="1.4"/></svg>
        info@webname.com
      </p>
    </div>

    <div class="front-brand">
      <span class="brand-dot"></span>
      <p class="brand-name">Signalpoint<br>Safety LLC</p>
    </div>

    <p class="address-block">421, Address line goes here<br>45452, Country Name</p>
    <div class="address-rule"></div>
    <p class="website">www.websitename.com</p>
  </section>

  <section class="card card-back" aria-label="Business card back">
    <div class="back-brand">
      <span class="brand-dot"></span>
      <p class="brand-name">Signalpoint<br>Safety LLC</p>
    </div>
  </section>

</main>
</body>
</html>
```